Update New Business Card - For Start Up

I need to update my business card, I have our old version for example. I would like to keep to the same colors and theme. We are a threat reporting and case management tool for corporations and educational institutions.

Target Market(s)

Corporate Security and Human Resources, School Administrators and Superintendents.

Industry/Entity Type

Physical Security and Technology.

Contact Information for Business Card

My Name, Founder/CEO, phone number 555-214-6082, Logo, Web...

Colors
0054AA
0677BA
7BADD7
CADEEF
E8F1F8

Requirements
Must have
• Something new and trendy.

```html
<!DOCTYPE html>
<html lang="en">
<head>
<meta charset="utf-8">
<title>Quorvane Business Card</title>
<link href="https://fonts.googleapis.com/css2?family=Open+Sans:wght@400;600&display=swap" rel="stylesheet">
<style>
  :root {
    --stage: #2b2b2b;
    --card-black: #121212;
    --brand-blue: #0677BA;
    --deep-blue: #0054AA;
    --sky-blue: #7BADD7;
    --mist: #CADEEF;
    --paper: #ffffff;
    --text-light: #d8d8d8;
  }
  * { margin: 0; padding: 0; box-sizing: border-box; }
  html, body { width: 1200px; height: 900px; overflow: hidden; }
  body {
    background: var(--stage);
    font-family: "Open Sans", sans-serif;
    position: relative;
  }
  .card {
    position: absolute;
    background: var(--card-black);
    border-radius: 22px;
    overflow: hidden;
  }

  /* Front (vertical) */
  .card-front {
    left: 150px; top: 150px;
    width: 350px; height: 600px;
  }
  .front-brand {
    position: absolute; left: 40px; top: 44px;
    display: flex; align-items: center; gap: 10px;
  }
  .brand-dot {
    flex: none;
    width: 26px; height: 26px; border-radius: 50%;
    background: var(--brand-blue);
  }
  .brand-name {
    color: var(--brand-blue);
    font-weight: 400;
    font-size: 22px;
    letter-spacing: 4px;
    text-transform: uppercase;
    white-space: nowrap;
  }
  .identity {
    position: absolute; left: 40px; top: 116px;
    padding-left: 14px;
    border-left: 5px solid var(--brand-blue);
  }
  .person-name {
    color: var(--brand-blue);
    font-weight: 600; font-size: 17px;
    text-transform: uppercase; letter-spacing: 0.5px;
  }
  .person-title { color: var(--text-light); font-size: 15px; margin-top: 2px; }
  .contact-list {
    position: absolute; left: 40px; top: 196px;
    list-style: none;
  }
  .contact-list li {
    display: flex; align-items: center; gap: 10px;
    color: var(--text-light); font-size: 15px; line-height: 27px;
    white-space: nowrap;
  }
  .contact-list svg { width: 13px; height: 13px; fill: var(--brand-blue); flex: none; }
  .front-panel {
    position: absolute; left: 0; right: 0; bottom: 0; height: 290px;
    background: var(--paper);
    border-top-left-radius: 175px;
    display: flex; align-items: center; justify-content: center;
  }
  .panel-circle {
    width: 230px; height: 230px; border-radius: 50%;
    background: var(--brand-blue);
    margin-top: 20px;
  }

  /* Back (horizontal) */
  .card-back {
    left: 560px; top: 150px;
    width: 560px; height: 330px;
    display: flex; align-items: center; justify-content: center;
  }
  .back-brand { display: flex; align-items: center; gap: 18px; }
  .back-brand .brand-dot { width: 56px; height: 56px; }
  .back-brand .brand-name { font-size: 40px; letter-spacing: 7px; }
</style>
</head>
<body>
  <section class="card card-front">
    <div class="front-brand">
      <span class="brand-dot"></span>
      <span class="brand-name">Quorvane</span>
    </div>
    <div class="identity">
      <p class="person-name">Alex Morrow</p>
      <p class="person-title">Founder/CEO</p>
    </div>
    <ul class="contact-list">
      <li><svg viewBox="0 0 24 24"><path d="M6.6 10.8a15 15 0 0 0 6.6 6.6l2.2-2.2a1 1 0 0 1 1-.25 11.4 11.4 0 0 0 3.6.57 1 1 0 0 1 1 1V20a1 1 0 0 1-1 1A17 17 0 0 1 3 4a1 1 0 0 1 1-1h3.5a1 1 0 0 1 1 1c0 1.25.2 2.45.57 3.6a1 1 0 0 1-.25 1z"/></svg>555-214-6082</li>
      <li><svg viewBox="0 0 24 24"><path d="M2 5h20v14H2z M4 7v.5l8 5 8-5V7z" fill-rule="evenodd"/></svg>alex@quorvane.co</li>
      <li><svg viewBox="0 0 24 24"><circle cx="12" cy="12" r="10"/></svg>www.quorvane.co</li>
    </ul>
    <div class="front-panel">
      <div class="panel-circle"></div>
    </div>
  </section>

  <section class="card card-back">
    <div class="back-brand">
      <span class="brand-dot"></span>
      <span class="brand-name">Quorvane</span>
    </div>
  </section>
</body>
</html>
```